BrookhavenLLC

Real Estate Investment. Buy/Sell house/investment . Trustworthy,Reliable, and friendly

Industry/Entity Type

Real Estate

Contact Information for Business Card

Brookhaven@mailbox-example.com
808-555-0143
Linnea-Joy Patterson

```html
<!DOCTYPE html>
<html lang="en">
<head>
<meta charset="utf-8">
<title>BrookhavenLLC – Business Card</title>
<link rel="stylesheet" href="https://fonts.googleapis.com/css2?family=Montserrat:wght@500;600;800&display=swap">
<style>
  :root {
    --page-bg: #e9ebee;
    --card-navy: #0b1d2e;
    --card-teal: #0f3340;
    --card-deep: #08141f;
    --text-light: #ffffff;
    --text-dark: #0d2233;
    --accent-blue: #1f7fd6;
    --accent-cyan: #1aa3b8;
    --accent-green: #1fa35a;
    --accent-deepgreen: #12704a;
  }
  * { margin: 0; padding: 0; box-sizing: border-box; }
  html, body {
    width: 1200px;
    height: 799px;
    overflow: hidden;
    background: var(--page-bg);
    font-family: "Montserrat", sans-serif;
  }
  .business-card {
    position: absolute;
    left: 75px;
    top: 100px;
    width: 1050px;
    height: 600px;
    overflow: hidden;
    box-shadow: 0 18px 40px rgba(0,0,0,0.25);
  }
  .card-backdrop {
    position: absolute;
    inset: 0;
    background:
      radial-gradient(circle at 48% 30%, rgba(40,110,120,0.35) 0%, rgba(40,110,120,0) 45%),
      radial-gradient(circle at 20% 80%, rgba(30,80,100,0.25) 0%, rgba(30,80,100,0) 40%),
      linear-gradient(135deg, var(--card-teal) 0%, var(--card-navy) 55%, var(--card-deep) 100%);
  }
  .accent-strip {
    position: absolute;
    display: flex;
    height: 12px;
  }
  .accent-strip span { height: 100%; }
  .accent-strip--top { top: 0; left: 560px; width: 490px; }
  .accent-strip--bottom { bottom: 0; left: 0; width: 470px; }
  .seg-deepgreen { background: var(--accent-deepgreen); }
  .seg-green { background: var(--accent-green); }
  .seg-cyan { background: var(--accent-cyan); }
  .seg-blue { background: var(--accent-blue); }

  .company-name {
    position: absolute;
    left: 430px;
    top: 218px;
    font-weight: 800;
    font-size: 58px;
    color: var(--text-light);
    letter-spacing: 0.5px;
  }
  .email-bar {
    position: absolute;
    left: 418px;
    top: 296px;
    width: 632px;
    height: 46px;
    background: var(--text-light);
    border-radius: 23px 0 0 23px;
    display: flex;
    align-items: center;
    padding-left: 22px;
  }
  .email {
    font-weight: 500;
    font-size: 26px;
    letter-spacing: 2px;
    color: var(--text-dark);
  }
  .person-name {
    position: absolute;
    left: 440px;
    top: 366px;
    font-weight: 800;
    font-size: 30px;
    letter-spacing: 3px;
    color: var(--text-light);
  }
  .phone-line {
    position: absolute;
    left: 440px;
    top: 414px;
    display: flex;
    align-items: center;
    gap: 8px;
    font-weight: 600;
    font-size: 27px;
    letter-spacing: 2px;
    color: var(--text-light);
  }
  .phone-icon { width: 28px; height: 28px; }
</style>
</head>
<body>
  <div class="business-card">
    <div class="card-backdrop" role="img" aria-label="Dark teal background with a faint pattern of overlapping circles"></div>

    <div class="accent-strip accent-strip--top">
      <span class="seg-deepgreen" style="width:200px"></span>
      <span class="seg-green" style="width:120px"></span>
      <span class="seg-cyan" style="width:60px"></span>
      <span class="seg-blue" style="width:110px"></span>
    </div>

    <h1 class="company-name">BrookhavenLLC</h1>

    <div class="email-bar">
      <span class="email">Brookhaven@mailbox-example.com</span>
    </div>

    <p class="person-name">Linnea-Joy Patterson</p>

    <p class="phone-line">
      <svg class="phone-icon" viewBox="0 0 28 28" aria-hidden="true">
        <circle cx="14" cy="14" r="14" fill="var(--accent-green)"/>
        <path d="M10 7.5c.6-.4 1.3-.2 1.6.4l1.2 2.3c.3.6.1 1.2-.4 1.6l-.9.6c.6 1.7 1.8 3 3.4 3.7l.7-.9c.4-.5 1.1-.6 1.6-.3l2.2 1.3c.6.3.8 1.1.4 1.6l-.9 1.3c-.5.7-1.4 1-2.2.8-4.2-1.1-7.4-4.4-8.5-8.6-.2-.8.1-1.6.8-2.1z" fill="var(--text-light)"/>
      </svg>
      808-555-0143
    </p>

    <div class="accent-strip accent-strip--bottom">
      <span class="seg-blue" style="width:140px"></span>
      <span class="seg-cyan" style="width:90px"></span>
      <span class="seg-green" style="width:120px"></span>
      <span class="seg-deepgreen" style="width:120px"></span>
    </div>
  </div>
</body>
</html>
```